Pemberly & Associates Tax Services

Need an eye catching advertisement/lead generating design for prospects interesting in professional tax planning and tax preparation services. Ideas for
Sample Advertising Language is below:

We are accepting new clients!!
We are affordable and have over 20 years of experience serving the tax needs of our clientele.

Here are a few reasons you may want to contact us:

1. You want to learn how to maximize business deductions
2. You’re a high-income earner and want to learn ways to pay less in taxes
3. You have an interest in starting a business
4. You want to maximize rental property deductions
5. You have questions about maintaining a home office
6. You want to be updated periodically on tax law changes and tax planning strategies
7. You want to be represented by a tax expert before the IRS if you are subject to an audit

References available upon request.

Target Market(s)

Individuals, small businesses and startup business

Industry/Entity Type

Tax and Accounting Industry

Requirements
Nice to have
• Would like to develop a marketing campaign that can be used periodically to digitally generate leads, build email contact list of prospective clients who want to receive tax updates.

```html
<!DOCTYPE html>
<html lang="en">
<head>
<meta charset="utf-8">
<title>Pemberly &amp; Associates – Accepting New Clients</title>
<link href="https://fonts.googleapis.com/css2?family=Bebas+Neue&family=Roboto+Condensed:wght@400;700&display=swap" rel="stylesheet">
<style>
  :root {
    --brand-blue: #1b5fa6;
    --deep-blue: #0f4a8c;
    --brand-green: #66c60a;
    --ink: #2e2e2e;
    --paper: #ffffff;
    --backdrop: #e8e5e0;
  }
  * { margin: 0; padding: 0; box-sizing: border-box; }
  html, body { width: 1200px; height: 900px; overflow: hidden; }
  body {
    background: var(--backdrop);
    font-family: "Roboto Condensed", "Arial Narrow", sans-serif;
    color: var(--ink);
    position: relative;
  }
  .flyer {
    position: absolute;
    left: 270px; top: 24px;
    width: 660px; height: 853px;
    background: var(--paper);
    overflow: hidden;
  }
  .hero { position: absolute; left: 0; top: 0; width: 660px; height: 530px; display: block; }
  .brand {
    position: absolute;
    left: 360px; top: 28px;
    display: flex; align-items: center; gap: 10px;
    color: var(--brand-blue);
    font-family: "Roboto Condensed", sans-serif;
    font-weight: 700;
  }
  .brand-dot { width: 46px; height: 46px; border-radius: 50%; background: var(--brand-blue); flex: none; }
  .brand-name { font-size: 25px; line-height: 24px; text-transform: uppercase; letter-spacing: 0.5px; }
  .brand-tag { font-size: 13px; line-height: 18px; text-transform: uppercase; letter-spacing: 0.6px; }
  .headline {
    position: absolute; left: 30px; top: 476px;
    font-family: "Bebas Neue", "Oswald", sans-serif;
    font-size: 58px; line-height: 54px;
    color: var(--brand-blue); font-weight: 400;
  }
  .pitch {
    position: absolute; left: 30px; top: 656px; width: 270px;
    font-size: 21px; line-height: 28px; font-weight: 700;
    color: var(--brand-blue);
  }
  .reasons { position: absolute; left: 318px; top: 500px; width: 320px; font-size: 14px; line-height: 18px; }
  .reasons-lead { font-weight: 700; margin-bottom: 6px; }
  .reasons ol { list-style: none; counter-reset: item; }
  .reasons li { counter-increment: item; padding-left: 20px; position: relative; margin-bottom: 4px; }
  .reasons li::before { content: counter(item) "."; position: absolute; left: 0; }
  .reasons-note { margin-top: 6px; }
  .footer { position: absolute; left: 0; bottom: 0; width: 660px; height: 49px; display: flex; }
  .footer-name {
    width: 316px; background: var(--brand-green); color: var(--ink);
    font-weight: 700; font-size: 13px; line-height: 16px;
    display: flex; flex-direction: column; align-items: center; justify-content: center;
  }
  .footer-contact {
    flex: 1; background: var(--brand-blue); color: var(--paper);
    font-size: 13px; line-height: 16px;
    display: flex; flex-direction: column; align-items: center; justify-content: center;
  }
</style>
</head>
<body>
  <article class="flyer">
    <svg class="hero" viewBox="0 0 660 530" xmlns="http://www.w3.org/2000/svg">
      <defs>
        <linearGradient id="heroPhoto" x1="0" y1="0" x2="1" y2="1">
          <stop offset="0" stop-color="#2a6bb4"/>
          <stop offset="0.45" stop-color="#1b5fa6"/>
          <stop offset="0.7" stop-color="#b7a48f"/>
          <stop offset="1" stop-color="#24324a"/>
        </linearGradient>
      </defs>
      <rect width="660" height="530" fill="url(#heroPhoto)" role="img" aria-label="Photo of a smiling couple meeting a tax advisor at a desk with a laptop, glass office towers behind"/>
      <path d="M290,0 L660,0 L660,150 C620,190 560,222 480,228 C395,230 330,190 290,110 Z" fill="var(--brand-green)"/>
      <path d="M317,0 L660,0 L660,113 C620,170 570,200 500,205 C420,206 350,150 317,70 Z" fill="var(--paper)"/>
      <path d="M0,410 C120,375 240,395 350,445 C460,495 560,490 660,425 L660,530 L0,530 Z" fill="var(--brand-green)"/>
      <path d="M0,462 C120,425 250,432 360,476 C455,508 560,500 660,455 L660,530 L0,530 Z" fill="var(--paper)"/>
    </svg>

    <div class="brand">
      <span class="brand-dot"></span>
      <div>
        <div class="brand-name">Pemberly &amp;<br>Associates LLC</div>
        <div class="brand-tag">Tax &amp; Business Services</div>
      </div>
    </div>

    <h1 class="headline">We are<br>accepting<br>new clients!!</h1>
    <p class="pitch">We are affordable and have over 20 years of experience serving the tax needs of our clientele.</p>

    <section class="reasons">
      <p class="reasons-lead">Here are a few reasons you may want to contact us:</p>
      <ol>
        <li>You want to learn how to maximize business deductions</li>
        <li>You're a high-income earner and want to learn ways to pay less in taxes</li>
        <li>You have an interest in starting a business</li>
        <li>You want to maximize rental property deductions</li>
        <li>You have questions about maintaining a home office</li>
        <li>You want to be updated periodically on tax law changes and tax planning strategies</li>
        <li>You want to be represented by a tax expert before the IRS if you are subject to an audit</li>
      </ol>
      <p class="reasons-note">References available upon request.</p>
    </section>

    <footer class="footer">
      <div class="footer-name"><span>Pemberly &amp; Associates</span><span>Tax and Business Services</span></div>
      <div class="footer-contact"><span>4180 Meadow Ridge Dr., Suite 210 Fairview, CA 95600</span><span>(555) 214-0386 &nbsp;|&nbsp; info@pemberlytax.com</span></div>
    </footer>
  </article>
</body>
</html>
```